Verpackungen für neue online Schokoladenmarke
Zielgruppe
Eine neue online Schokoladenmarke deren Zielgruppe sind anspruchsvolle Schokoladenliebhaber,
denn die Schokolade wird aus Kakaobohnen langzeitgewalzt.
Die Käufer essen nicht süß, sondern wünschen den wirklichen Kakaobohnengeschmack ohne
Zusatzstoffe.
Die Schokolade wird nur online verkauft.
Aufgabenstellung
Markenname: nib4tab Chocolate ---------- oder----- NIB4TAB Chocolate oder ?
Der Markenname soll dominant sein, und die Vorderseite eines Tafelkartons prägen, als
Umverpackung 80 x 160 mm - die Vorderseite, nur die ist hier beauftragt.
Obwohl Bio, muss die Verpackung nicht recycelt oder 'alternativ' aussehen, nicht im Öko - Design auftreten.
Bitte keine angebissenen Schokotafeln, Sahnetöpfe oder sonstige altmodischen Grafiken nutzen.
Der Firmenname nib4tab soll (gut lesbar) gestaltet werden, in Groß- oder Kleinbuchstaben etc. Eventuell
einen Bezug auf Online haben, oder auch nicht...
Der Gewinner kann ggf. weitere Designaufträge und auch die Layouts bzw. Datenübergabe für den
Kartonhersteller machen. Dauerbetreuung erwünscht..!

```html
<!DOCTYPE html>
<html lang="en">
<head>
<meta charset="utf-8">
<title>nib4tab dark chocolate – front panel</title>
<link rel="stylesheet" href="https://fonts.googleapis.com/css2?family=Quicksand:wght@400;700&display=swap">
<style>
  :root {
    --navy: #172f3f;
    --ornament-light: #4a7186;
    --ornament-dark: #1f3d4e;
    --gold: #f2bd1f;
    --gold-deep: #d89e0c;
    --label-fill: rgba(23, 47, 63, 0.55);
  }
  html, body {
    margin: 0;
    padding: 0;
    width: 1200px;
    height: 2400px;
    overflow: hidden;
    background: var(--navy);
  }
  .pack-front {
    position: relative;
    width: 1200px;
    height: 2400px;
    background: var(--navy);
    font-family: "Quicksand", sans-serif;
    overflow: hidden;
  }
  .ornament-layer {
    position: absolute;
    inset: 0;
  }
  .brand-ring {
    position: absolute;
    left: 203px;
    top: 222px;
    width: 788px;
    height: 788px;
    border: 6px solid var(--gold);
    border-radius: 50%;
    box-sizing: border-box;
  }
  .brand-name {
    position: absolute;
    left: 0;
    width: 1200px;
    top: 500px;
    text-align: center;
    font-size: 200px;
    font-weight: 700;
    line-height: 1;
    color: var(--gold);
    letter-spacing: 2px;
    margin: 0;
  }
  .variety-label {
    position: absolute;
    left: 203px;
    top: 1579px;
    width: 809px;
    height: 383px;
    box-sizing: border-box;
    border: 4px solid var(--gold-deep);
    background: var(--label-fill);
    color: var(--gold);
    text-align: center;
    font-weight: 400;
    font-size: 152px;
    line-height: 178px;
    padding-top: 12px;
    margin: 0;
  }
  .variety-label span { display: block; }
  .edition-number {
    position: absolute;
    right: 88px;
    top: 2030px;
    font-size: 260px;
    font-weight: 400;
    line-height: 1;
    color: var(--gold);
  }
  .net-weight {
    position: absolute;
    left: 236px;
    top: 2318px;
    font-size: 52px;
    font-weight: 700;
    color: var(--gold);
    line-height: 1;
  }
</style>
</head>
<body>
  <main class="pack-front">
    <svg class="ornament-layer" width="1200" height="2400" viewBox="0 0 1200 2400">
      <defs>
        <linearGradient id="ornamentTone" x1="0" y1="0" x2="0" y2="1">
          <stop offset="0" stop-color="var(--ornament-light)"/>
          <stop offset="0.5" stop-color="var(--ornament-dark)"/>
          <stop offset="1" stop-color="var(--ornament-light)"/>
        </linearGradient>
      </defs>
      <rect class="ornament-band-top" x="0" y="0" width="1200" height="133"
            fill="url(#ornamentTone)" role="img" aria-label="Floral scroll ornament in muted blue"/>
      <polygon class="ornament-field" points="1200,908 0,1283 0,2299 1200,2299"
               fill="url(#ornamentTone)" role="img" aria-label="Flowing floral scroll ornament in muted blue"/>
    </svg>

    <div class="brand-ring"></div>
    <h1 class="brand-name">nib4tab</h1>

    <h2 class="variety-label"><span>dark</span><span>choclate</span></h2>

    <div class="edition-number">4</div>
    <div class="net-weight">100g</div>
  </main>
</body>
</html>
```